Ecommerce site that acts also as a portal for B2C members and non- members and B2B. Please see attachment this is for only front end work, backend will follow. Husk and Kettle- a MRWE Hospitality Company

Products
Coffee bean sourcing, acquisition, roasting, grinding, blending, sale/delivery
Tea sourcing, acquisition, roasting, grinding, blending, sale/delivery
Applicable/Associated Merchandise and Accoutrements

Initial market penetration for both B2C and B2B offering Husk and Kettle custom blends of both Coffees and Teas.
B2C- Brindle style sale/distribution via guest and members. Members initial fee $129 annual $99 a year thereafter with benefits such as 1st year gift of a French Press Travel Mug (customized/logo/name/brand), monthly samples. Attached document has non project related information for narrative and conceptual inputs.

```html
<!DOCTYPE html>
<html lang="en">
<head>
<meta charset="utf-8">
<title>Husk and Kettle — Artisan Coffee &amp; Tea</title>
<link href="https://fonts.googleapis.com/css2?family=Poppins:wght@400;500;600;700&display=swap" rel="stylesheet">
<style>
:root{
  --brown:#b47a2c;
  --brown-deep:#8b5a1f;
  --brown-dark:#6e4515;
  --band:#c0842f;
  --cream:#f3e5d6;
  --ink:#2a2420;
  --muted:#4a423c;
  --white:#ffffff;
  --hero:#141312;
}
*{box-sizing:border-box;margin:0;padding:0}
html,body{width:1200px;height:4399px;overflow:hidden}
body{font-family:"Poppins",sans-serif;color:var(--ink);background:var(--white);position:relative}
.abs{position:absolute}
.btn{position:absolute;display:flex;align-items:center;justify-content:center;border-radius:30px;font-size:10px;font-weight:600;letter-spacing:.3px;text-transform:uppercase}
.btn-fill{background:linear-gradient(180deg,#a36a22,var(--brown-dark));color:var(--white)}
.btn-line{border:1.5px solid var(--brown-deep);color:var(--brown-dark);background:var(--white)}
.title{color:var(--brown);font-weight:600;text-transform:uppercase;text-align:center;font-size:24px;letter-spacing:.2px}
.copy{font-size:12px;line-height:19px;color:var(--muted)}
.photo{position:absolute;overflow:hidden}

/* header */
.site-header{position:absolute;left:0;top:0;width:1200px;height:70px}
.brand-badge{position:absolute;left:100px;top:-4px;width:100px;height:106px;border-radius:0 0 50px 50px;background:var(--white);display:flex;align-items:center;justify-content:center;text-align:center;z-index:3}
.brand-badge span{color:var(--brown-dark);font-weight:600;font-size:13px;line-height:15px;text-transform:uppercase}
.main-nav{position:absolute;left:366px;top:29px;display:flex;gap:20px;font-size:10px;font-weight:500;text-transform:uppercase}
.nav-icons{position:absolute;left:893px;top:29px;display:flex;gap:10px}

/* hero */
.hero{position:absolute;left:0;top:70px;width:1200px;height:696px;border-radius:100px;background:var(--hero);overflow:hidden}
.hero-art{position:absolute;left:380px;top:70px;width:820px;height:626px;background:radial-gradient(ellipse at 60% 55%,#5a3a22 0%,#2e211a 35%,#171513 70%)}
.hero-eyebrow{left:118px;top:210px;color:var(--white);font-size:13px;font-weight:600;letter-spacing:2.5px}
.hero h1{position:absolute;left:118px;top:232px;color:var(--white);font-size:45px;line-height:50px;font-weight:600;text-transform:uppercase;width:520px}
.hero-text{left:118px;top:399px;color:#e6e1dc;font-size:12.5px;line-height:19px;width:380px}

/* about */
.about-heading{left:440px;top:966px;width:350px;font-size:23px}
.about-text{left:474px;top:1015px;width:284px;text-align:center}

/* blends */
.blend-card{position:absolute;top:1511px;width:177px;height:264px;border-radius:90px 90px 40px 40px;background:var(--white);box-shadow:0 6px 18px rgba(0,0,0,.12);overflow:hidden;text-align:center}
.blend-card .photo{left:8px;top:8px;width:161px;height:137px;border-radius:80px 80px 0 0}
.blend-card h3{position:absolute;left:0;top:172px;width:100%;color:var(--brown);font-size:14px;font-weight:600}
.blend-card p{position:absolute;left:20px;top:196px;width:137px;font-size:10px;line-height:15px;color:var(--muted)}

/* custom band */
.custom-band{position:absolute;left:0;top:1941px;width:1200px;height:375px;background:var(--band);border-radius:80px;overflow:hidden}
.step-num{position:absolute;top:44px;font-size:72px;font-weight:600;color:transparent;-webkit-text-stroke:2px rgba(255,255,255,.8);line-height:1}
.step-card{position:absolute;top:97px;width:189px;height:213px;background:var(--white);border-radius:14px}
.step-card svg{position:absolute;left:20px;top:32px}
.step-card h3{position:absolute;left:20px;bottom:26px;color:var(--brown);font-size:13.5px;line-height:15px;font-weight:600;text-transform:uppercase}

/* members */
.feature-title{color:var(--brown);font-size:23px;line-height:28px;font-weight:600;text-transform:uppercase}

/* journal */
.journal{position:absolute;left:0;top:3163px;width:1200px;height:649px;background:var(--cream);border-radius:90px 90px 0 90px}
.story h3{color:var(--brown);font-size:17px;font-weight:600;text-transform:uppercase}
.read-more{font-size:10px;font-weight:600;color:var(--brown-dark);text-decoration:underline;text-transform:uppercase}

/* footer */
.footer-col h4{font-size:12px;font-weight:600;text-transform:uppercase;color:var(--ink);margin-bottom:14px}
.footer-col li{list-style:none;font-size:10px;line-height:18.7px;color:var(--muted)}
.social{display:flex;gap:8px}
.social span{width:17px;height:17px;border-radius:50%;background:var(--brown)}
</style>
</head>
<body>

<header class="site-header">
  <div class="brand-badge"><span>Husk<br>and<br>Kettle</span></div>
  <nav class="main-nav">
    <span>Home</span><span>Hop</span><span>Custom Blends</span><span>Membership</span><span>Wholesale</span><span>About Us</span><span>Blog</span>
  </nav>
  <div class="nav-icons">
    <svg width="10" height="10" viewBox="0 0 10 10" fill="none" stroke="#555" stroke-width="1.2"><circle cx="4.2" cy="4.2" r="3.2"/><path d="M6.6 6.6 9.4 9.4"/></svg>
    <svg width="10" height="10" viewBox="0 0 10 10" fill="none" stroke="#555" stroke-width="1.2"><circle cx="5" cy="3.2" r="2.2"/><path d="M1 9.5c.5-2.5 2-3.5 4-3.5s3.5 1 4 3.5"/></svg>
    <svg width="10" height="10" viewBox="0 0 10 10" fill="none" stroke="#555" stroke-width="1.2"><path d="M1.5 3h7l-.6 6.4H2.1z"/><path d="M3.5 3V2a1.5 1.5 0 0 1 3 0v1"/></svg>
  </div>
  <div class="btn btn-fill" style="left:978px;top:20px;width:101px;height:32px">Contact Us</div>
</header>

<section class="hero">
  <div class="hero-art" role="img" aria-label="Dark moody still life of a coffee bag, a mug and a glass of coffee with scattered roasted beans and grounds"></div>
  <p class="abs hero-eyebrow">WELCOME TO HUSK AND KETTLE</p>
  <h1>Artisan Coffee &amp; Tea, Crafted for Connoisseurs</h1>
  <p class="abs hero-text">Explore exclusive blends, premium teas, and custom roasts curated for taste, aroma, and sophistication.</p>
  <div class="btn btn-fill" style="left:118px;top:454px;width:100px;height:28px">Shop Now</div>
  <div class="btn" style="left:226px;top:454px;width:130px;height:28px;border:1.5px solid #fff;color:#fff">Join Membership</div>
</section>

<section class="about">
  <div class="photo" style="left:118px;top:881px;width:321px;height:428px;border-radius:10px;background:linear-gradient(180deg,#d99a4a 0%,#9a6a2e 40%,#3e3a1c 100%)" role="img" aria-label="Sunrise over rows of coffee plants on a plantation"></div>
  <h2 class="abs title about-heading">Luxury in Every Sip</h2>
  <p class="abs copy about-text">Husk and Kettle, a MRWE Hospitality Company, sources the finest coffee beans and tea leaves worldwide. From meticulous roasting to expert blending, we craft unique flavors for both discerning individuals and business partners. Our passion for quality ensures every cup tells a story of refinement, aroma, and indulgence.</p>
  <div class="btn btn-fill" style="left:565px;top:1193px;width:101px;height:29px">Read More</div>
  <div class="photo" style="left:804px;top:879px;width:222px;height:260px;border-radius:8px;background:linear-gradient(135deg,#8a9aa8,#5e6e7c 60%,#7a4a3a)" role="img" aria-label="Wooden spoons with dried tea and coffee on a slate surface"></div>
  <div class="photo" style="left:838px;top:1120px;width:239px;height:196px;border-radius:8px;background:linear-gradient(135deg,#5a3a3c,#3a2224 60%,#6e4a3c);border:3px solid #fff" role="img" aria-label="Coffee beans spilling from a burlap sack beside a hand grinder"></div>
</section>

<section class="blends">
  <h2 class="abs title" style="left:0;top:1395px;width:1200px">Discover Our Signature Blends</h2>
  <p class="abs copy" style="left:390px;top:1443px;width:420px;text-align:center">From bold, rich coffees to delicate, aromatic teas, each selection is designed to delight your palate.</p>
  <article class="blend-card" style="left:225px"><div class="photo" style="background:linear-gradient(160deg,#6e4a2c,#3a2618)" role="img" aria-label="Cups filled with roasted coffee beans"></div><h3>COFFEE BLENDS</h3><p>Single Origin · Espresso · Custom Roast</p></article>
  <article class="blend-card" style="left:418px"><div class="photo" style="background:linear-gradient(160deg,#d8d6d0,#b08a52)" role="img" aria-label="Bowls of loose-leaf teas and a glass of amber tea"></div><h3>TEA BLENDS</h3><p>Herbal · Green · Black · Seasonal</p></article>
  <article class="blend-card" style="left:607px"><div class="photo" style="background:linear-gradient(160deg,#4a2a2c,#2a1c1c)" role="img" aria-label="Assorted coffee accessories and gift items"></div><h3>ACCESSORIES</h3><p>French Press · Travel Mugs · Brewing Gear</p></article>
  <article class="blend-card" style="left:799px"><div class="photo" style="background:linear-gradient(160deg,#9aa4ac,#5a5450)" role="img" aria-label="Open gift box with coffee and tea items"></div><h3>GIFT SETS</h3><p>Curated Boxes · Corporate Gifting</p></article>
  <div class="btn btn-fill" style="left:527px;top:1815px;width:144px;height:30px">View All Products</div>
</section>

<section class="custom-band">
  <h2 class="abs" style="left:118px;top:150px;color:#fff;font-size:23px;font-weight:600">YOUR BLEND, YOUR WAY</h2>
  <p class="abs" style="left:118px;top:190px;width:330px;color:#fff;font-size:11.5px;line-height:19px">Select your beans, roast, and flavor notes for a coffee or tea experience that's truly yours.</p>
  <div class="btn" style="left:118px;top:251px;width:203px;height:30px;background:#fff;color:var(--ink)">Create Your Custom Blend</div>
  <span class="step-num" style="left:555px">01</span>
  <span class="step-num" style="left:756px">02</span>
  <span class="step-num" style="left:957px">03</span>
  <div class="step-card" style="left:487px">
    <svg width="56" height="70" viewBox="0 0 56 70"><rect x="8" y="0" width="20" height="20" rx="4" fill="#8b5a1f"/><rect x="30" y="0" width="20" height="20" rx="4" fill="#8b5a1f"/><path d="M12 28v26c0 8 6 14 14 14h6c8 0 12-6 12-14V40c0-3-4-3-4 0v-4c0-3-4-3-4 0v-2c0-3-4-3-4 0V28c0-4-6-4-6 0v14h-2V28c0-4-6-4-6 0z" fill="#8b5a1f"/></svg>
    <h3>Choose Beans<br>or Leaves</h3>
  </div>
  <div class="step-card" style="left:688px">
    <svg width="80" height="70" viewBox="0 0 80 70"><path d="M28 6l5 5 10-10" stroke="#8b5a1f" stroke-width="3" fill="none"/><circle cx="14" cy="32" r="6" fill="#8b5a1f"/><circle cx="36" cy="26" r="8" fill="#8b5a1f"/><circle cx="58" cy="32" r="6" fill="#8b5a1f"/><path d="M2 62c0-12 5-20 12-20s12 8 12 20zM22 62c0-16 6-26 14-26s14 10 14 26zM46 62c0-12 5-20 12-20s12 8 12 20z" fill="#8b5a1f"/></svg>
    <h3>Select Roast or<br>Steep Style</h3>
  </div>
  <div class="step-card" style="left:889px">
    <svg width="70" height="64" viewBox="0 0 70 64" fill="#8b5a1f"><rect x="2" y="8" width="66" height="5" rx="2.5"/><rect x="2" y="30" width="66" height="5" rx="2.5"/><rect x="2" y="52" width="66" height="5" rx="2.5"/><circle cx="46" cy="10.5" r="9"/><circle cx="22" cy="32.5" r="9"/><circle cx="50" cy="54.5" r="9"/></svg>
    <h3>Customize<br>Packaging or<br>Gift Options</h3>
  </div>
</section>

<section class="membership">
  <div class="photo" style="left:31px;top:2429px;width:287px;height:353px;border-radius:6px;background:linear-gradient(135deg,#d8d2c8,#a0703a 60%,#7a5a3a)" role="img" aria-label="Couple sharing mugs of coffee at home"></div>
  <h2 class="abs feature-title" style="left:353px;top:2497px;width:320px">Become a Husk<br>and Kettle Member</h2>
  <p class="abs copy" style="left:355px;top:2567px;width:280px">Enjoy exclusive perks as a member: monthly samples, early access to new blends, and a complimentary French Press Travel Mug in your first year. Membership starts at $129 the first year and $99 annually thereafter.</p>
  <div class="btn btn-fill" style="left:355px;top:2685px;width:102px;height:29px">Join Now</div>
  <div class="btn btn-line" style="left:468px;top:2685px;width:227px;height:29px">Learn More About Membership</div>

  <div class="photo" style="left:744px;top:2429px;width:287px;height:353px;border-radius:6px;background:linear-gradient(135deg,#3a3430,#1e1b19 60%,#6a5a48)" role="img" aria-label="Barista in a cafe holding takeaway cups and a paper bag"></div>
  <h2 class="abs feature-title" style="left:1067px;top:2497px;width:320px">Wholesale<br>Partnerships</h2>
  <p class="abs copy" style="left:1067px;top:2567px;width:280px">Our B2B program provides flexible bulk ordering, custom blends for cafes, restaurants, and hotels. Elevate your brand with our products.</p>
  <div class="btn btn-fill" style="left:1068px;top:2685px;width:102px;height:29px">Learn More</div>
  <div class="btn btn-line" style="left:1180px;top:2685px;width:150px;height:29px"></div>
</section>

<section class="testimonials">
  <h2 class="abs title" style="left:0;top:2882px;width:1200px">What Our Customers &amp; Partners Say</h2>
  <p class="abs copy" style="left:340px;top:2929px;width:520px;text-align:center">From the very first brew, I could tell this was something special. The aroma is deep and inviting, and the flavor profile is incredibly smooth yet bold. Husk and Kettle has completely transformed my daily coffee ritual—every morning now feels like a café-quality experience at home."</p>
  <svg class="abs" style="left:568px;top:3026px" width="64" height="12" viewBox="0 0 64 12" fill="#d9a232"><g id="s"><path d="M6 0l1.8 3.8 4.2.5-3.1 2.9.8 4.1L6 9.3 2.3 11.3l.8-4.1L0 4.3l4.2-.5z"/></g><use href="#s" x="13"/><use href="#s" x="26"/><use href="#s" x="39"/><use href="#s" x="52"/></svg>
  <svg class="abs" style="left:577px;top:3060px" width="46" height="8" viewBox="0 0 46 8"><circle cx="4" cy="4" r="3" fill="#b9b4ae"/><circle cx="16" cy="4" r="3" fill="#2a2420"/><circle cx="28" cy="4" r="3" fill="#b9b4ae"/><circle cx="40" cy="4" r="3" fill="#b9b4ae"/></svg>
</section>

<section class="journal">
  <h2 class="abs title" style="left:0;top:65px;width:1200px">Brewing Tips &amp; Flavor Stories</h2>
  <article class="photo" style="left:171px;top:140px;width:370px;height:405px;border-radius:8px;background:linear-gradient(160deg,#3e4a58,#1c2026 60%,#2a2420)" role="img" aria-label="Barista pouring from a gooseneck kettle into a pour-over dripper">
    <h3 class="abs" style="left:23px;top:270px;color:#fff;font-size:17px;font-weight:600">COFFEE BREWING GUIDES</h3>
    <p class="abs" style="left:23px;top:298px;width:315px;color:#fff;font-size:11.5px;line-height:19px">Explore the art and science behind exceptional coffee and tea. From expert brewing techniques to seasonal flavor inspirations, our stories are d...</p>
    <span class="abs read-more" style="left:23px;top:361px;color:#fff">Read More</span>
  </article>
  <div class="photo" style="left:556px;top:140px;width:217px;height:196px;border-radius:8px;background:linear-gradient(160deg,#2a2420,#7a4a2a 70%,#c8a070)" role="img" aria-label="Tea being poured from a clay teapot into small cups"></div>
  <div class="photo" style="left:556px;top:350px;width:217px;height:195px;border-radius:8px;background:linear-gradient(160deg,#6a5a6a,#7a4a2a 60%,#3a2a2a)" role="img" aria-label="Close-up of dried seasonal tea leaves"></div>
  <div class="abs story" style="left:800px;top:166px;width:280px">
    <h3>Tea Steeping Techniques</h3>
    <p class="copy" style="margin-top:8px;font-size:11.5px">Learn how to brew café-quality coffee at home or in professional settings. Our step-by-step guides cover everything from grind size and water temperature to brewing...</p>
    <span class="read-more" style="display:block;margin-top:14px">Read More</span>
  </div>
  <div class="abs story" style="left:800px;top:376px;width:280px">
    <h3>Seasonal Blend Highlights</h3>
    <p class="copy" style="margin-top:8px;font-size:11.5px">Unlock the full character of premium tea leaves with our expert steeping tips. Discover the ideal temperatures, steeping times, and serving suggestions for green, black, herbal...</p>
    <span class="read-more" style="display:block;margin-top:14px">Read More</span>
  </div>
</section>

<section class="newsletter">
  <h2 class="abs title" style="left:0;top:3904px;width:1200px">Join Our Inner Circle</h2>
  <p class="abs" style="left:0;top:3944px;width:1200px;text-align:center;font-size:10.5px;color:var(--muted)">Get new arrivals, exclusive offers, and luxury updates before anyone else.</p>
  <div class="abs" style="left:336px;top:3986px;width:512px;height:41px;border-radius:22px;background:#fff;box-shadow:0 3px 12px rgba(0,0,0,.1)">
    <svg class="abs" style="left:22px;top:17px" width="9" height="7" viewBox="0 0 9 7"><rect width="9" height="7" rx="1" fill="#8b5a1f"/></svg>
    <span class="abs" style="left:36px;top:13px;font-size:10px;color:var(--muted)">Email field</span>
    <div class="btn btn-fill" style="left:374px;top:5px;width:121px;height:31px">Subscribe Now</div>
  </div>
</section>

<footer class="site-footer">
  <div class="abs" style="left:171px;top:4140px;width:130px;text-align:center;color:var(--brown-dark);font-size:27px;line-height:32px;font-weight:600;text-transform:uppercase">Husk<br><span style="font-size:16px;line-height:18px">and</span><br>Kettle</div>
  <div class="abs footer-col" style="left:401px;top:4120px"><h4>Quick Links</h4><ul><li>Home</li><li>Shop</li><li>Custom Blends</li><li>Membership</li><li>Wholesale</li><li>About Us</li><li>Blog</li><li>Contact</li></ul></div>
  <div class="abs footer-col" style="left:579px;top:4120px;width:200px"><h4>Contact Us</h4>
    <div style="display:flex;gap:10px;font-size:10px;color:var(--muted);margin-bottom:8px"><svg width="10" height="10" viewBox="0 0 10 10"><path d="M2 0l2 2.5-1 1.5c.7 1.3 1.7 2.3 3 3l1.5-1L10 8 8.5 10C4 9.5.5 6 0 1.5z" fill="#8b5a1f"/></svg>(555)014-2291</div>
    <div style="display:flex;gap:10px;font-size:10px;color:var(--muted);margin-bottom:8px"><svg width="10" height="8" viewBox="0 0 10 8"><rect width="10" height="8" rx="1" fill="#8b5a1f"/></svg>hello@huskandkettle.example</div>
    <div style="display:flex;gap:10px;font-size:10px;line-height:12px;color:var(--muted)"><svg width="10" height="12" viewBox="0 0 10 12"><path d="M5 0a4.5 4.5 0 0 1 4.5 4.5C9.5 8 5 12 5 12S.5 8 .5 4.5A4.5 4.5 0 0 1 5 0z" fill="#8b5a1f"/><circle cx="5" cy="4.5" r="1.6" fill="#fff"/></svg><span>418 Alderwick Lane Fairhollow,<br>CA 90000</span></div>
  </div>
  <div class="abs footer-col" style="left:818px;top:4120px;width:180px"><h4>Subscribe for Updates</h4>
    <p style="font-size:10px;line-height:13px;color:var(--muted)">Subscribe and be the first to receive all the latest insights.</p>
    <p style="margin-top:14px;font-size:8px;color:#aaa;border-bottom:1px solid #ddd;padding-bottom:4px">EMAIL</p>
  </div>
  <div class="btn btn-fill" style="left:819px;top:4235px;width:99px;height:29px">Subscribe</div>
  <div class="abs" style="left:142px;top:4341px;width:916px;height:1px;background:#e5e0da"></div>
  <p class="abs" style="left:142px;top:4360px;font-size:9px;color:var(--brown-dark)">© Husk and Kettle, a MRWE Hospitality Company. All Rights Reserved.</p>
  <div class="abs social" style="left:938px;top:4356px"><span></span><span></span><span></span><span></span><span></span></div>
  <svg class="abs" style="left:1136px;top:4324px" width="34" height="32" viewBox="0 0 34 32"><path d="M17 2C8 2 2 7.5 2 14c0 4 2.3 7.5 6 9.6L7 30l7-4.3c1 .2 2 .3 3 .3 9 0 15-5.5 15-12S26 2 17 2z" fill="#8b5a1f"/><circle cx="11" cy="14" r="2" fill="#fff"/><circle cx="17" cy="14" r="2" fill="#fff"/><circle cx="23" cy="14" r="2" fill="#fff"/></svg>
</footer>

</body>
</html>
```